Ember Ridge Clearing postcard ( for direct mailing) and business card design

Design postcards/Business cards
Dale Horvick
Ember Ridge Clearing
482 Copperfern Rd Lewisville,NC 27023
(336) 555-0184 Dale@Emberridgeclearing.example

The postcard will be used for direct mailing to land owners and contractors to advertise our service. Pictures of the process and equipment along with a short summary of what we do. Business card should be contact info and logo.
Updates

The post cards could say something like this: Forestry Mulching machines are capable of clearing land of unwanted trees and brush with limited disturbance to soils or desirable vegetation. Traditional land clearing methods often present an increased risk of erosion by pushing over trees, uprooting the stump and roots, and substantially disturbing soils.In contrast, mulching the vegetation leaves the soil structure intact. The mulched material can be left on the ground and will act as an erosion barrier while returning nutrients back into the soil through decomposition. Over time, grass will naturally grow through the mulch and can be maintained with mowing.

Target Market(s)

Land owners and contractors who need vegetation cleared

Industry/Entity Type

Forestry Mulching

Requirements
Must have
• picture, brief description of service offered, contact info on postcard. Business card should have contact info and logo.
Nice to have
• I like contour lines as a background but I'd like to see other ideas.

```html
<!DOCTYPE html>
<html lang="en">
<head>
<meta charset="utf-8">
<title>Ember Ridge Clearing – Business Card</title>
<link href="https://fonts.googleapis.com/css2?family=Montserrat:wght@500;600;800&display=swap" rel="stylesheet">
<style>
  :root {
    --canvas: #e9e7e2;
    --card: #f7f7f5;
    --ink: #1e1e1e;
    --band: #231f20;
    --green-dark: #137a2f;
    --green-mid: #2f9a3a;
    --green-light: #6cc04a;
    --rule: #c9c9c9;
    --white: #ffffff;
  }
  * { box-sizing: border-box; margin: 0; padding: 0; }
  html, body { width: 1200px; height: 705px; overflow: hidden; }
  body {
    background: var(--canvas);
    font-family: "Montserrat", Arial, sans-serif;
    color: var(--ink);
    position: relative;
  }
  .card {
    position: absolute;
    top: 210px;
    width: 500px;
    height: 286px;
    background: var(--card);
    overflow: hidden;
    box-shadow: 0 6px 18px rgba(0,0,0,.18);
  }
  .card--front { left: 70px; }
  .card--back { left: 630px; }

  .corner { position: absolute; display: block; }
  .corner--top { left: 0; top: 0; width: 110px; height: 100px; }
  .corner--bottom { right: 0; bottom: 20px; width: 70px; height: 70px; }

  .band {
    position: absolute;
    left: 0; right: 0; bottom: 24px;
    height: 34px;
    background: var(--band);
    color: var(--white);
    display: flex;
    align-items: center;
    font-size: 15px;
    font-weight: 500;
    letter-spacing: .5px;
  }

  .wordmark {
    font-weight: 800;
    text-transform: uppercase;
    color: var(--ink);
    line-height: .98;
    letter-spacing: 1px;
  }

  /* Front */
  .card--front .wordmark {
    position: absolute;
    left: 110px; top: 82px;
    font-size: 30px;
  }
  .card--front .band { padding-left: 110px; gap: 28px; }
  .phone { display: flex; align-items: center; gap: 8px; }
  .phone svg { width: 15px; height: 15px; }

  /* Back */
  .card--back .wordmark {
    position: absolute;
    left: 58px; top: 96px;
    font-size: 22px;
  }
  .divider {
    position: absolute;
    left: 232px; top: 28px;
    width: 1px; height: 170px;
    background: var(--rule);
  }
  .contact {
    position: absolute;
    left: 252px; top: 40px;
    list-style: none;
  }
  .contact__name {
    color: var(--green-dark);
    font-weight: 800;
    font-size: 17px;
    margin-bottom: 12px;
    text-transform: uppercase;
  }
  .contact__row {
    display: flex;
    align-items: flex-start;
    gap: 8px;
    font-size: 11px;
    line-height: 1.45;
    margin-bottom: 8px;
  }
  .contact__row svg { flex: 0 0 14px; width: 14px; height: 14px; margin-top: 1px; }
  .card--back .band { padding-left: 58px; font-size: 14px; text-transform: uppercase; }
</style>
</head>
<body>

<article class="card card--front">
  <svg class="corner corner--top" viewBox="0 0 110 100"><polygon points="0,0 110,0 0,100" fill="var(--green-dark)"/></svg>
  <h1 class="wordmark">Ember<br>Ridge<br>Clearing</h1>
  <div class="band">
    <span class="name">DALE HORVICK</span>
    <span class="phone">
      <svg viewBox="0 0 16 16"><circle cx="8" cy="8" r="7" fill="none" stroke="#fff" stroke-width="1.2"/><path d="M5.5 4.5l1.5 0 .6 2-1 .8a5 5 0 0 0 2.2 2.2l.8-1 2 .6v1.5c0 .5-.4.8-.9.8A6.5 6.5 0 0 1 4.6 5.4c0-.5.4-.9.9-.9z" fill="#fff"/></svg>
      (336) 555-0184
    </span>
  </div>
  <svg class="corner corner--bottom" viewBox="0 0 70 70"><polygon points="70,0 70,70 0,70" fill="var(--green-light)"/></svg>
</article>

<article class="card card--back">
  <svg class="corner corner--top" viewBox="0 0 110 100"><polygon points="0,0 110,0 0,100" fill="var(--green-dark)"/></svg>
  <h2 class="wordmark">Ember<br>Ridge<br>Clearing</h2>
  <div class="divider"></div>
  <ul class="contact">
    <li class="contact__name">Dale Horvick</li>
    <li class="contact__row">
      <svg viewBox="0 0 14 14"><circle cx="7" cy="7" r="7" fill="var(--ink)"/><path d="M4.8 3.8h1.2l.5 1.6-.8.6a4 4 0 0 0 1.8 1.8l.6-.8 1.6.5v1.2c0 .4-.3.6-.7.6A5.2 5.2 0 0 1 4.2 4.5c0-.4.2-.7.6-.7z" fill="#fff"/></svg>
      (336) 555-0184
    </li>
    <li class="contact__row">
      <svg viewBox="0 0 14 14"><circle cx="7" cy="7" r="7" fill="var(--ink)"/><rect x="3.5" y="4.5" width="7" height="5" fill="none" stroke="#fff" stroke-width="1"/><path d="M3.5 4.5l3.5 3 3.5-3" fill="none" stroke="#fff" stroke-width="1"/></svg>
      Dale@Emberridgeclearing.example
    </li>
    <li class="contact__row">
      <svg viewBox="0 0 14 14"><circle cx="7" cy="7" r="7" fill="var(--ink)"/><path d="M7 3a2.4 2.4 0 0 1 2.4 2.4C9.4 7.4 7 10.5 7 10.5S4.6 7.4 4.6 5.4A2.4 2.4 0 0 1 7 3z" fill="#fff"/><circle cx="7" cy="5.4" r=".9" fill="var(--ink)"/></svg>
      <span>482 Copperfern Rd Alder Bend,<br>NC 27099</span>
    </li>
  </ul>
  <div class="band">Forestry Mulching &amp; Land Clearing</div>
  <svg class="corner corner--bottom" viewBox="0 0 70 70"><polygon points="70,0 70,70 0,70" fill="var(--green-light)"/></svg>
</article>

</body>
</html>
```